Owen Tasker Studios Business Card

Looking for a clear, modern, elegant, sharp business card that conveys a professional yet edgy image to my business as a wedding, portrait, and travel photographer. Would like something that looks vintage yet modern. Need a new business card to grow my business. We are growing the business for Wedding and Event Photography as well as fine art Photography. (Mostly Landscapes)
Updates

I’m looking through designs now but I have a new logo that i want using please.

New logo uploaded please redesign using that

PLEASE ALL DESIGNERS LOOK IN BRIEF FOR NEW LOGO

Target Market(s)

Brides, Grooms, Families with Kids, People looking for Fine Art Photography Artwork

Industry/Entity Type

Photographer

Contact Information for Business Card

Unsure

Font styles to use
Serif

Colors

Designer to choose colors to be used in the design.

Requirements
Must have
• My Website:
• http://taskerlens.examplefolio.net
• Phone:
• 323-481-5206
• Email:
• owentaskerlens@mailbox-example.net
Nice to have
• Would like a sort of shine on the printing finish.
• I like black I think it looks good on a business card.
• Can try working with my logo (png that I've attached)

```html
<!DOCTYPE html>
<html lang="en">
<head>
<meta charset="utf-8">
<title>Owen Tasker Studios Business Card</title>
<link rel="stylesheet" href="https://fonts.googleapis.com/css2?family=Questrial&display=swap">
<style>
  :root {
    --page: #ffffff;
    --card-dark: #1a1a1a;
    --card-light: #e0e0e0;
    --ink-light: #f2f2f2;
    --ink-dark: #1c1c1c;
  }
  html, body {
    margin: 0;
    padding: 0;
    width: 1200px;
    height: 1000px;
    overflow: hidden;
    background: var(--page);
  }
  .canvas {
    position: relative;
    width: 1200px;
    height: 1000px;
    font-family: "Questrial", "Century Gothic", sans-serif;
  }
  .card {
    position: absolute;
    left: 304px;
    width: 626px;
    height: 358px;
  }
  .card--front {
    top: 126px;
    background: var(--card-dark);
    color: var(--ink-light);
  }
  .card--back {
    top: 516px;
    background: var(--card-light);
    color: var(--ink-dark);
  }
  .brand-square {
    position: absolute;
    left: 272px;
    top: 97px;
    width: 74px;
    height: 74px;
    border: 1.5px solid var(--ink-light);
    box-sizing: border-box;
  }
  .brand-name {
    position: absolute;
    left: 0;
    right: 0;
    top: 196px;
    margin: 0;
    text-align: center;
    font-weight: 400;
    font-size: 35px;
    line-height: 1;
    letter-spacing: 0.01em;
  }
  .brand-sub {
    position: absolute;
    left: 0;
    right: 0;
    top: 243px;
    margin: 0;
    text-align: center;
    font-size: 16px;
    line-height: 1;
    letter-spacing: 0.6em;
    padding-left: 0.6em;
  }
  .back-name {
    position: absolute;
    left: 22px;
    bottom: 30px;
    margin: 0;
    font-size: 30px;
    line-height: 1;
  }
  .contact {
    position: absolute;
    right: 27px;
    top: 248px;
    margin: 0;
    text-align: right;
    font-style: normal;
    font-size: 15.5px;
    line-height: 20px;
  }
  .contact span { display: block; }
</style>
</head>
<body>
  <main class="canvas">
    <section class="card card--front" aria-label="Card front">
      <div class="brand-square" aria-hidden="true"></div>
      <h1 class="brand-name">OWEN TASKER</h1>
      <p class="brand-sub">STUDIOS</p>
    </section>

    <section class="card card--back" aria-label="Card back">
      <p class="back-name">Owen Tasker Studios</p>
      <address class="contact">
        <span>323-481-5206</span>
        <span>taskerlens.examplefolio.net</span>
        <span>owentaskerlens@mailbox-example.net</span>
      </address>
    </section>
  </main>
</body>
</html>
```